Business Card Design

I would like a new business card design for an accounting firm that specializes in resolving clients tax problems. I want the card to give the impression that we are not your typical stodgy accounting firm, but at the same time we will get the job done.
Industry/Entity Type
Business
Contact Information for Business Card
Dorian T Welsby
Certified Public Accountant
38-27 52nd Street
Sunnyside, NY 11287
Tel: (718) 555-0142
Fax: (888) 555-0199
e-mail: dtwthecpa@ledgerpost.com
website: harborfilingreliefexperts.com

```html
<!DOCTYPE html>
<html lang="en">
<head>
<meta charset="utf-8">
<title>Dorian T Welsby – Business Card</title>
<link rel="stylesheet" href="https://fonts.googleapis.com/css2?family=Jost:wght@400&family=Tinos:wght@400;700&display=swap">
<style>
  :root {
    --paper: #ffffff;
    --brand-blue: #0a7fc4;
    --ink: #111111;
    --key-black: #121314;
    --key-grey: #3d4144;
    --key-text: #ffffff;
    --key-border: #b9b9b9;
  }
  html, body { margin: 0; padding: 0; overflow: hidden; background: var(--paper); }
  .card {
    position: relative;
    width: 704px;
    height: 1200px;
    background: var(--paper);
    overflow: hidden;
    font-family: "Tinos", "Times New Roman", serif;
    color: var(--ink);
  }
  .identity-icon { position: absolute; left: 35px; top: 66px; width: 40px; height: 44px; }
  .name {
    position: absolute; left: 99px; top: 56px; margin: 0;
    font-family: "Jost", "Futura", sans-serif; font-weight: 400;
    font-size: 57px; line-height: 1; color: var(--brand-blue); letter-spacing: 0.3px;
  }
  .title {
    position: absolute; left: 196px; top: 124px; margin: 0;
    font-size: 25.5px; line-height: 1;
  }
  .contact-list { position: absolute; left: 0; top: 0; margin: 0; padding: 0; list-style: none; }
  .contact-item {
    position: absolute; left: 36px; display: flex; align-items: center; white-space: nowrap;
    font-size: 35px; line-height: 1;
  }
  .contact-item svg { width: 34px; height: 30px; margin-right: 19px; flex: none; }
  .contact-item.address { font-size: 29px; }
  .keypad { position: absolute; left: 0; top: 0; }
  .key {
    position: absolute; display: flex; align-items: center; justify-content: center;
    color: var(--key-text); font-weight: 700; font-size: 31px; box-sizing: border-box;
  }
  .key.fn { background: var(--brand-blue); }
  .key.digit { background: var(--key-black); }
  .key.soft { background: var(--key-grey); }
  .key.blank { background: var(--key-black); border: 2px solid var(--key-border); }
  .c1 { left: 54px; width: 144px; }
  .c2 { left: 209px; width: 143px; }
  .c3 { left: 368px; width: 143px; }
  .c4 { left: 521px; width: 143px; }
  .r1 { top: 557px; height: 92px; }
  .r2 { top: 663px; height: 92px; }
  .r3 { top: 768px; height: 93px; }
  .r4 { top: 875px; height: 92px; }
  .r5 { top: 978px; height: 92px; }
  .r6 { top: 1083px; height: 94px; }
  .key.equals { left: 523px; width: 144px; top: 1085px; height: 96px; }
</style>
</head>
<body>
<div class="card">
  <svg class="identity-icon" viewBox="0 0 40 44" aria-hidden="true">
    <ellipse cx="20" cy="13" rx="9" ry="11" fill="var(--ink)"/>
    <path d="M2 44 C2 30 9 26 15 25 L20 31 L25 25 C31 26 38 30 38 44 Z" fill="var(--ink)"/>
  </svg>
  <h1 class="name">Dorian T Welsby</h1>
  <p class="title">Certified Public Accountant</p>

  <ul class="contact-list">
    <li class="contact-item" style="top:345px">
      <svg viewBox="0 0 34 30" aria-hidden="true"><path d="M25 2 L31 7 C26 10 22 15 20 19 C17 24 12 27 8 29 L3 24 L8 19 L12 22 C15 19 18 15 20 11 L16 8 Z" fill="var(--ink)"/></svg>
      <span>(718) 555-0142</span>
    </li>
    <li class="contact-item" style="top:387px">
      <svg viewBox="0 0 34 30" aria-hidden="true"><rect x="9" y="1" width="16" height="8" fill="var(--ink)"/><rect x="3" y="10" width="28" height="13" rx="2" fill="var(--ink)"/><rect x="9" y="19" width="16" height="10" fill="var(--ink)"/><rect x="11" y="21" width="12" height="2" fill="#fff"/><rect x="11" y="25" width="12" height="2" fill="#fff"/></svg>
      <span>(888) 555-0199</span>
    </li>
    <li class="contact-item" style="top:430px">
      <svg viewBox="0 0 34 30" aria-hidden="true"><rect x="3" y="6" width="28" height="19" fill="none" stroke="var(--ink)" stroke-width="2"/><path d="M3 6 L17 18 L31 6 M3 25 L13 15 M31 25 L21 15" fill="none" stroke="var(--ink)" stroke-width="2"/></svg>
      <span>dtwthecpa@ledgerpost.com</span>
    </li>
    <li class="contact-item" style="top:471px">
      <svg viewBox="0 0 34 30" aria-hidden="true"><circle cx="17" cy="15" r="12" fill="none" stroke="var(--ink)" stroke-width="2.5"/><ellipse cx="17" cy="15" rx="5" ry="12" fill="none" stroke="var(--ink)" stroke-width="2"/><path d="M5 11 H29 M5 19 H29" stroke="var(--ink)" stroke-width="2"/></svg>
      <span>www.harborfilingreliefexperts.com</span>
    </li>
    <li class="contact-item address" style="top:512px">
      <svg viewBox="0 0 34 30" aria-hidden="true"><path d="M17 2 L3 14 H7 V29 H27 V14 H31 Z" fill="var(--ink)"/><rect x="13" y="18" width="8" height="11" fill="#fff"/></svg>
      <span>38-27, 52nd Street Brookvale, Ny 11287.</span>
    </li>
  </ul>

  <div class="keypad">
    <div class="key fn c1 r1">MC</div>
    <div class="key fn c2 r1">MR</div>
    <div class="key fn c3 r1">MS</div>
    <div class="key fn c4 r1">M+</div>

    <div class="key fn c1 r2">C</div>
    <div class="key fn c2 r2">±</div>
    <div class="key fn c3 r2">%</div>
    <div class="key fn c4 r2">÷</div>

    <div class="key digit c1 r3">7</div>
    <div class="key digit c2 r3">8</div>
    <div class="key digit c3 r3">9</div>
    <div class="key fn c4 r3">X</div>

    <div class="key digit c1 r4">4</div>
    <div class="key digit c2 r4">5</div>
    <div class="key digit c3 r4">6</div>
    <div class="key fn c4 r4">−</div>

    <div class="key digit c1 r5">1</div>
    <div class="key digit c2 r5">2</div>
    <div class="key digit c3 r5">3</div>
    <div class="key fn c4 r5">+</div>

    <div class="key blank c1 r6"></div>
    <div class="key soft c2 r6">0</div>
    <div class="key soft c3 r6">.</div>
    <div class="key digit equals">=</div>
  </div>
</div>
</body>
</html>
```